5 Email Newsletter Templates Needed

We need 5 email templates for our email marketing campaign. We are an Insurance Agency in Los Angeles called KDP-Silverbrook Insurance Services. We use Mailvane Hub as our email marketing platform. The templates need to be simple, a nice header, not to busy and you will need to use our color palette. The first email template we need is for our current clients / prospects. The content we will put in this email will be insurance tips and information, short and simple about 2 small paragraphs. The next 3 templates all need to be the same but different colors. One red, one yellow and one green. These will be alerts from kdp-silverbrook. An example a major earthquake hits we will send a red alert. A legislative change on healthcare and we send a yellow alert. We buy another location and we send a green alert. The last email is for our COINs (Centers of Influence, the people who refer business to us). I uploaded an email from one of our business consultants to give an idea of the size and sophistication we are looking for. I also uploaded our corporate brochure and color palette so you can learn more about our firm.

Target Market(s)

Our target markets are commercial business 1mm plus in revenue, 500 employees, high net worth individuals. Our COINs are CPAs, CFOs, Business Managers

Requirements
Nice to have
• HTML Code is desired. You can also provide just an image file for the header and our email marketing program will do the coding for us.
Should not have
• No cartoon looking graphics. Do not use old-style fonts like Times New Roman.

```html
<!DOCTYPE html>
<html lang="en">
<head>
<meta charset="utf-8">
<title>Green Alert – KDP-Silverbrook Insurance Services</title>
<link rel="stylesheet" href="https://fonts.googleapis.com/css2?family=Arimo:wght@400;700&display=swap">
<style>
  :root {
    --page-bg: #cdcdc8;
    --card-bg: #ffffff;
    --header-top: #f4f4f4;
    --header-bottom: #dedede;
    --brand-dark: #00594b;
    --alert-green: #34cc68;
    --body-text: #333333;
    --muted-text: #8a8a8a;
    --footer-text: #ffffff;
    --icon-blue: #3b5998;
    --icon-sky: #5bb7db;
  }
  * { box-sizing: border-box; margin: 0; padding: 0; }
  html, body {
    width: 1167px;
    height: 1200px;
    overflow: hidden;
    background: var(--page-bg);
    font-family: "Arimo", Arial, sans-serif;
  }
  .canvas { position: relative; width: 1167px; height: 1200px; }

  .online-link {
    position: absolute;
    top: 114px;
    left: 0;
    width: 100%;
    text-align: center;
    font-size: 16px;
    color: var(--footer-text);
    text-decoration: underline;
  }

  .email-card {
    position: absolute;
    left: 85px;
    top: 167px;
    width: 997px;
    height: 816px;
    background: var(--card-bg);
    box-shadow: 0 4px 14px rgba(0,0,0,0.45);
  }

  .email-header {
    position: absolute;
    left: 0; top: 0;
    width: 100%;
    height: 76px;
    background: linear-gradient(var(--header-top), var(--header-bottom));
  }
  .brand {
    position: absolute;
    left: 45px;
    top: 35px;
    display: flex;
    align-items: center;
    gap: 12px;
  }
  .brand-mark {
    width: 22px;
    height: 22px;
    background: var(--brand-dark);
  }
  .brand-name {
    font-size: 27px;
    font-weight: 400;
    letter-spacing: 1px;
    color: var(--brand-dark);
  }
  .header-band {
    position: absolute;
    left: 0; top: 76px;
    width: 100%;
    height: 17px;
    background: var(--brand-dark);
  }

  .alert-banner {
    position: absolute;
    left: -2px;
    top: 150px;
    width: 959px;
    height: 150px;
  }
  .alert-title {
    position: absolute;
    left: 243px;
    top: 202px;
    font-size: 50px;
    font-weight: 400;
    color: #ffffff;
  }

  .social {
    position: absolute;
    left: 65px;
    top: 323px;
    width: 120px;
    text-align: center;
  }
  .social-label { font-size: 17px; color: var(--muted-text); }
  .social-icons {
    margin-top: 16px;
    display: flex;
    justify-content: center;
    gap: 9px;
  }
  .social-icon { width: 26px; height: 26px; border-radius: 4px; }
  .social-icon--one { background: var(--icon-blue); }
  .social-icon--two { background: var(--icon-sky); }

  .alert-body {
    position: absolute;
    left: 245px;
    top: 360px;
    width: 640px;
    font-size: 20.5px;
    line-height: 33.5px;
    color: var(--body-text);
  }
  .alert-body p + p { margin-top: 33.5px; }

  .email-footer {
    position: absolute;
    left: 100px;
    top: 1000px;
    font-size: 17px;
    line-height: 24.5px;
    color: var(--footer-text);
  }
  .unsubscribe {
    position: absolute;
    right: 120px;
    top: 996px;
    font-size: 16px;
    color: var(--footer-text);
    text-decoration: underline;
  }
</style>
</head>
<body>
<div class="canvas">
  <a class="online-link">View the online version</a>

  <main class="email-card">
    <header class="email-header">
      <div class="brand">
        <span class="brand-mark"></span>
        <span class="brand-name">KDP-SILVERBROOK INSURANCE SERVICES</span>
      </div>
    </header>
    <div class="header-band"></div>

    <svg class="alert-banner" viewBox="0 0 959 150" aria-hidden="true">
      <polygon points="0,0 925,0 959,75 925,150 0,150" fill="var(--alert-green)"/>
    </svg>
    <h1 class="alert-title">Green Alert</h1>

    <aside class="social">
      <div class="social-label">Follow Us</div>
      <div class="social-icons">
        <span class="social-icon social-icon--one"></span>
        <span class="social-icon social-icon--two"></span>
      </div>
    </aside>

    <section class="alert-body">
      <p>Lorem ipsum dolor sit amet, consectetuer adipiscing elit, sed diam nonummy nibh euismod tincidunt ut laoreet dolore magna aliquam erat volutpat. Ut wisi enim ad minim veniam, quis nostrud exerci tation ullamcorper suscipit lobortis nisl ut aliquip ex ea commodo consequat.</p>
      <p>Duis autem vel eum iriure dolor in hendrerit in vulputate velit esse molestie consequat, vel illum dolore eu feugiat nulla facilisis at vero eros et accumsan et iusto odio dignissim qui blandit praesent luptatum zzril delenit augue duis dolore te feugait nulla facilisi.</p>
    </section>
  </main>

  <address class="email-footer" style="font-style:normal">
    Northcrest Continuity Group<br>
    4870 Larkspur Ave - Suite 210B<br>
    Maplewood, OR 97402<br>
    555.218.4730
  </address>
  <a class="unsubscribe">Unsubscribe</a>
</div>
</body>
</html>
```